Urine collection cup with and without sterile seal sticker

Hello. We need a urine cup label designed please with

Name:
Date of Birth:
Date:
Time:
Temp℃:
Specimen ID:

Product code: TUB-47
Volume markings (e.g., 30 mL, 60 mL, 90 mL).
Vela Drug Tests logo

Could you please provide one version with the additional sterile sticker extending to the top, and one version without the additional sterile sticker?

```html
<!DOCTYPE html>
<html lang="en">
<head>
<meta charset="utf-8">
<title>Vela Drug Tests – Urine Cup Labels</title>
<link href="https://fonts.googleapis.com/css2?family=Roboto:wght@500;700&display=swap" rel="stylesheet">
<style>
  :root {
    --navy: #13284f;
    --navy-deep: #0d1f45;
    --orange: #f26a1b;
    --seal: #574b8c;
    --placeholder: #c9cdd8;
    --paper: #ffffff;
  }
  * { box-sizing: border-box; margin: 0; padding: 0; }
  html, body { width: 1200px; height: 800px; overflow: hidden; background: var(--paper); }
  body { position: relative; font-family: "Roboto", Arial, sans-serif; color: var(--navy); }

  .label {
    position: absolute; top: 91px; width: 545px; height: 647px;
    border: 2.5px solid var(--navy); border-radius: 26px; background: var(--paper);
  }
  .label--sealed { left: 34px; }
  .label--plain { left: 623px; }

  .brand { position: absolute; left: 44px; top: 42px; display: flex; align-items: center; gap: 12px; }
  .label--plain .brand { top: 52px; }
  .brand__dot { width: 44px; height: 44px; border-radius: 50%; background: var(--orange); }
  .brand__name { font-size: 25px; font-weight: 700; color: var(--navy); letter-spacing: 0.2px; }

  .fields { position: absolute; left: 21px; top: 136px; width: 390px; }
  .label--plain .fields { left: 21px; top: 150px; width: 382px; }
  .field { display: flex; align-items: flex-end; height: 36px; margin-bottom: 26.5px; }
  .field__icon { width: 36px; height: 36px; flex: none; }
  .field__label { font-size: 17px; font-weight: 500; margin-left: 12px; line-height: 1; padding-bottom: 9px; white-space: nowrap; }
  .field__line { flex: 1; border-bottom: 1px solid var(--navy); margin-left: 10px; height: 26px; position: relative; }
  .field__hint { position: absolute; right: 4px; bottom: 2px; font-size: 13px; color: var(--placeholder); letter-spacing: 0.5px; }
  .dob { flex: 1; display: flex; align-items: flex-end; margin-left: 10px; }
  .dob__part { border-bottom: 1px solid var(--navy); height: 26px; text-align: center; font-size: 13px; color: var(--placeholder); line-height: 34px; }
  .dob__part--d, .dob__part--m { width: 42px; }
  .dob__part--y { flex: 1; max-width: 69px; margin-left: auto; }
  .dob__sep { font-size: 16px; font-weight: 700; width: 28px; text-align: center; padding-bottom: 2px; }

  .code { background: var(--paper); border: 2px solid var(--navy); border-radius: 4px; padding: 13px 0 0 14px; }
  .code__title { font-size: 13px; font-weight: 500; }
  .code__value { font-size: 28px; font-weight: 700; line-height: 1.2; }

  .volumes { position: absolute; display: flex; }
  .volume { display: flex; flex-direction: column; align-items: center; border-left: 1.5px solid var(--navy); }
  .volume__drop { width: 22px; height: 29px; }
  .volume__text { font-size: 18px; font-weight: 700; margin-top: 14px; }

  .label--sealed .code { position: absolute; left: 25px; top: 534px; width: 128px; height: 82px; border-bottom: 8px solid var(--orange); }
  .label--sealed .volumes { left: 168px; top: 540px; height: 71px; }
  .label--sealed .volume { width: 87.5px; padding-top: 6px; }

  .footer-box { position: absolute; left: 42px; top: 529px; width: 474px; height: 93px; border: 1.5px solid var(--navy); border-radius: 14px; }
  .label--plain .code { position: absolute; left: 13px; top: 6px; width: 127px; height: 79px; background: var(--navy-deep); border-color: var(--navy-deep); color: var(--paper); }
  .label--plain .volumes { left: 158px; top: 10px; height: 72px; }
  .label--plain .volume { width: 105.5px; padding-top: 8px; }

  .scale { position: absolute; left: 431px; top: 15px; width: 100px; height: 165px; overflow: visible; }
  .scale__text { font-size: 16px; font-weight: 700; fill: var(--navy); font-family: "Roboto", Arial, sans-serif; }

  .seal { position: absolute; left: 445px; top: 48px; width: 111px; height: 716px; }
  .seal__tab { position: absolute; left: 0; top: 0; width: 111px; height: 70px; background: var(--seal); border-radius: 18px; display: flex; align-items: center; justify-content: center; color: var(--paper); font-size: 17px; font-weight: 700; letter-spacing: 0.3px; }
  .seal__strip { position: absolute; left: 25px; top: 60px; width: 57px; height: 656px; background: var(--seal); border-radius: 0 0 6px 6px; }
  .seal__text { position: absolute; left: 50%; top: 118px; transform: translateX(-50%); writing-mode: vertical-rl; color: var(--paper); font-size: 16.5px; font-weight: 700; letter-spacing: 0.6px; white-space: nowrap; }
  .seal__check { position: absolute; left: 8px; top: 582px; width: 41px; height: 41px; }
</style>
</head>
<body>
<svg width="0" height="0" style="position:absolute" aria-hidden="true">
  <defs>
    <symbol id="icon-person" viewBox="0 0 36 36"><circle cx="18" cy="18" r="18" fill="#13284f"/><circle cx="18" cy="14" r="4.5" fill="#fff"/><path d="M10 26c0-5 3.5-7.5 8-7.5s8 2.5 8 7.5z" fill="#fff"/></symbol>
    <symbol id="icon-calendar" viewBox="0 0 36 36"><circle cx="18" cy="18" r="18" fill="#13284f"/><rect x="9" y="10" width="18" height="16" rx="1.5" fill="#fff"/><rect x="9" y="10" width="18" height="3.5" fill="#cfd5e2"/><path d="M11 16h14M11 19.5h14M11 23h14M13.5 14v11M17 14v11M20.5 14v11M24 14v11" stroke="#13284f" stroke-width="0.9"/></symbol>
    <symbol id="icon-calendar-clock" viewBox="0 0 36 36"><circle cx="18" cy="18" r="18" fill="#13284f"/><rect x="8" y="9" width="17" height="15" rx="1.5" fill="#fff"/><path d="M10 14.5h13M10 18h13M10 21.5h13M12.5 12.5v10M16 12.5v10M19.5 12.5v10" stroke="#13284f" stroke-width="0.9"/><circle cx="24.5" cy="24" r="4.8" fill="#fff" stroke="#13284f" stroke-width="1.2"/><path d="M24.5 21.5v2.7h2" stroke="#13284f" stroke-width="1.1" fill="none"/></symbol>
    <symbol id="icon-clock" viewBox="0 0 36 36"><circle cx="18" cy="18" r="18" fill="#13284f"/><circle cx="18" cy="18" r="10" fill="#fff"/><circle cx="18" cy="18" r="8" fill="none" stroke="#13284f" stroke-width="1"/><path d="M18 12.5v5.5l3.5 2" stroke="#13284f" stroke-width="1.5" fill="none" stroke-linecap="round"/></symbol>
    <symbol id="icon-thermo" viewBox="0 0 36 36"><circle cx="18" cy="18" r="18" fill="#13284f"/><path d="M15 9.5a2.5 2.5 0 0 1 5 0v10.5a4.5 4.5 0 1 1-5 0z" fill="#fff"/><circle cx="17.5" cy="23.5" r="2.3" fill="#13284f"/><rect x="16.8" y="12" width="1.4" height="10" fill="#13284f"/><path d="M22 11h3M22 14h2.5M22 17h3" stroke="#fff" stroke-width="1.1"/></symbol>
    <symbol id="icon-id" viewBox="0 0 36 36"><circle cx="18" cy="18" r="18" fill="#13284f"/><rect x="9" y="12" width="18" height="13" rx="1" fill="none" stroke="#fff" stroke-width="1.4"/><rect x="11.5" y="15" width="6" height="7" fill="#fff"/><path d="M19.5 16h5M19.5 18.5h5M19.5 21h4" stroke="#fff" stroke-width="1.2"/><path d="M15 12v-2h6v2" stroke="#fff" stroke-width="1.2" fill="none"/></symbol>
    <symbol id="icon-drop" viewBox="0 0 22 29"><path d="M11 0C8 7 1 13 1 19a10 10 0 0 0 20 0C21 13 14 7 11 0z" fill="#13284f"/><path d="M15.5 19a4.5 4.5 0 0 1-3.5 5" stroke="#fff" stroke-width="1.6" fill="none" stroke-linecap="round"/></symbol>
  </defs>
</svg>

<!-- Version with sterile seal -->
<section class="label label--sealed">
  <div class="brand"><span class="brand__dot"></span><span class="brand__name">Vela Drug Tests</span></div>
  <div class="fields">
    <div class="field"><svg class="field__icon"><use href="#icon-person"/></svg><span class="field__label">Name:</span><span class="field__line"></span></div>
    <div class="field"><svg class="field__icon"><use href="#icon-calendar"/></svg><span class="field__label">Date of Birth:</span>
      <span class="dob"><span class="dob__part dob__part--d">DD</span><span class="dob__sep">/</span><span class="dob__part dob__part--m">MM</span><span class="dob__sep">/</span><span class="dob__part dob__part--y">YYYY</span></span></div>
    <div class="field"><svg class="field__icon"><use href="#icon-calendar-clock"/></svg><span class="field__label">Date:</span><span class="field__line"></span></div>
    <div class="field"><svg class="field__icon"><use href="#icon-clock"/></svg><span class="field__label">Time:</span><span class="field__line"><span class="field__hint">AM / PM</span></span></div>
    <div class="field"><svg class="field__icon"><use href="#icon-thermo"/></svg><span class="field__label">Temp°C:</span><span class="field__line"></span></div>
    <div class="field"><svg class="field__icon"><use href="#icon-id"/></svg><span class="field__label">Specimen ID:</span><span class="field__line"></span></div>
  </div>
  <div class="code"><p class="code__title">Product code:</p><p class="code__value">TUB-47</p></div>
  <div class="volumes">
    <div class="volume"><svg class="volume__drop"><use href="#icon-drop"/></svg><span class="volume__text">30 ML</span></div>
    <div class="volume"><svg class="volume__drop"><use href="#icon-drop"/></svg><span class="volume__text">60 ML</span></div>
    <div class="volume"><svg class="volume__drop"><use href="#icon-drop"/></svg><span class="volume__text">90 ML</span></div>
  </div>
</section>

<div class="seal">
  <div class="seal__strip">
    <span class="seal__text">INTERIOR AS LONG AS SEAL REMAINS INTACT</span>
    <svg class="seal__check" viewBox="0 0 41 41"><circle cx="20.5" cy="20.5" r="18.5" fill="none" stroke="#fff" stroke-width="2.6"/><path d="M12.5 21l5.5 5.5 10.5-11" fill="none" stroke="#fff" stroke-width="2.8" stroke-linecap="round" stroke-linejoin="round"/></svg>
  </div>
  <div class="seal__tab">STERILE</div>
</div>

<!-- Version without seal -->
<section class="label label--plain">
  <div class="brand"><span class="brand__dot"></span><span class="brand__name">Vela Drug Tests</span></div>
  <svg class="scale" viewBox="0 -10 100 165">
    <path d="M4 1.5h24M16 1.5v141M8 71.5h20M4 142.5h24" stroke="#13284f" stroke-width="1.6" fill="none"/>
    <text class="scale__text" x="35" y="7">90 ML</text>
    <text class="scale__text" x="35" y="77">60 ML</text>
    <text class="scale__text" x="35" y="148">30 ML</text>
  </svg>
  <div class="fields">
    <div class="field"><svg class="field__icon"><use href="#icon-person"/></svg><span class="field__label">Name:</span><span class="field__line"></span></div>
    <div class="field"><svg class="field__icon"><use href="#icon-calendar"/></svg><span class="field__label">Date of Birth:</span>
      <span class="dob"><span class="dob__part dob__part--d">DD</span><span class="dob__sep">/</span><span class="dob__part dob__part--m">MM</span><span class="dob__sep">/</span><span class="dob__part dob__part--y">YYYY</span></span></div>
    <div class="field"><svg class="field__icon"><use href="#icon-calendar-clock"/></svg><span class="field__label">Date:</span><span class="field__line"></span></div>
    <div class="field"><svg class="field__icon"><use href="#icon-clock"/></svg><span class="field__label">Time:</span><span class="field__line"><span class="field__hint">AM / PM</span></span></div>
    <div class="field"><svg class="field__icon"><use href="#icon-thermo"/></svg><span class="field__label">Temp°C:</span><span class="field__line"></span></div>
    <div class="field"><svg class="field__icon"><use href="#icon-id"/></svg><span class="field__label">Specimen ID:</span><span class="field__line"></span></div>
  </div>
  <div class="footer-box">
    <div class="code"><p class="code__title">Product code:</p><p class="code__value">TUB-47</p></div>
    <div class="volumes">
      <div class="volume"><svg class="volume__drop"><use href="#icon-drop"/></svg><span class="volume__text">30 ML</span></div>
      <div class="volume"><svg class="volume__drop"><use href="#icon-drop"/></svg><span class="volume__text">60 ML</span></div>
      <div class="volume"><svg class="volume__drop"><use href="#icon-drop"/></svg><span class="volume__text">90 ML</span></div>
    </div>
  </div>
</section>
</body>
</html>
```